Creative Web Design - Intl Market Research Company

We need an innovative web design for an emerging company into the international market research marketplace.

The company, Velmoran Associates, is a Trade, Investment, and Market Research company. Velmoran offers domestic and international companies increased success in the U.S. marketplace by providing a variety of services. (seen on attached brochure)

The website should be cutting edge and creative while having an easy navigation. The color is not fixed and attached logo is not finalized, feel free to post anything from conservative to progressive options. Keep in mind target customers are domestic and international businesses looking to emerge/improve in the U.S. marketplace.

Additional Company information is located in the attached documentation. The documentation is outdated & winner will have priority standing for our next projects.(logo & document re-design)
Updates

I have received a few e-mail requests and have updated the status to guaranteed payment.

Thanks!

Target Market(s)

Any company, foreign and domestic, looking to introduce their product into the U.S. marketplace.

Industry/Entity Type

Market Research

Requirements
Must have
• Easy Navigation
Should not have
• Too many buttons
Difficult navigation
Excessive Typography

```html
<!DOCTYPE html>
<html lang="en">
<head>
<meta charset="utf-8">
<title>Velmoran Associates — Trade, Investment, Market Research</title>
<link rel="stylesheet" href="https://fonts.googleapis.com/css2?family=PT+Sans+Narrow:wght@400;700&family=Source+Sans+3:wght@400;600;700&display=swap">
<style>
:root{
  --red:#c60000;
  --ink:#333333;
  --text:#2b2b2b;
  --muted:#555555;
  --card:#e8e8e8;
  --card-line:#d2d2d2;
  --btn:#d4d4d4;
  --icon:#bdbdbd;
  --line:#e2e2e2;
  --footer:#232323;
  --white:#ffffff;
}
*{box-sizing:border-box;margin:0;padding:0}
html,body{width:996px;height:1200px;overflow:hidden;background:var(--white)}
body{position:relative;font-family:"Source Sans 3",Arial,sans-serif;color:var(--text)}
.abs{position:absolute}

/* header */
.brand{left:73px;top:44px;display:flex;align-items:center;gap:16px}
.brand-mark{width:50px;height:50px;border-radius:50%;background:#b59a4e}
.brand-name{font-family:"PT Sans Narrow",Arial,sans-serif;font-weight:700;font-size:24px;color:var(--ink);line-height:1}
.brand-tag{font-size:12px;color:var(--ink);margin-top:8px}
.search{left:737px;top:22px;width:189px;height:28px;border:1px solid #c9c9c9;border-radius:3px;font-size:11px;font-style:italic;color:#999;padding:6px 0 0 5px}
.search svg{position:absolute;right:9px;top:7px}
.nav{right:70px;top:71px;display:flex;gap:0;font-size:14px;font-weight:600;color:var(--ink)}
.nav a{color:inherit;text-decoration:none;padding:5px 14px;height:27px}
.nav a.active{background:var(--red);color:var(--white);border-radius:2px;padding:5px 11px;margin-right:6px}
.nav a:last-child{padding-right:0}

/* hero */
.hero{left:0;top:120px;width:996px;height:351px;border-top:1px solid var(--line);border-bottom:1px solid var(--line);
  background:linear-gradient(90deg,#f1efec 0%,#e9e4dc 35%,#e7d8c4 55%,#b8cfd8 70%,#d9c4ad 85%,#f3efea 100%)}
.hero-copy{left:144px;top:226px}
.hero-title{font-family:"PT Sans Narrow",Arial,sans-serif;font-weight:700;font-size:30px;color:var(--ink);line-height:1}
.hero-sub{font-size:19px;color:var(--ink);margin-top:8px;letter-spacing:.2px}
.hero-text{font-size:13.5px;line-height:21px;color:var(--ink);margin-top:9px;width:250px}
.dots{left:877px;top:451px;display:flex;gap:3px}
.dots span{width:8px;height:8px;border-radius:50%;background:#444}
.dots span:first-child{background:#fff;border:1px solid #444}

/* service cards */
.card{top:501px;width:193px;height:257px;background:var(--card);text-align:center;padding:10px 13px 0}
.card h3{font-size:17px;font-weight:600;line-height:21px;color:#555;text-transform:uppercase;height:51px;border-bottom:1px solid var(--card-line)}
.card svg{display:block;margin:8px auto 0}
.card p{font-size:12px;line-height:18px;color:var(--ink);margin-top:14px}
.card .more{display:inline-block;margin-top:12px;background:var(--btn);color:#444;font-size:13.5px;padding:5px 18px;width:113px}
.card.is-active{background:var(--red)}
.card.is-active h3{color:var(--white);border-color:#e25a5a}
.card.is-active p{color:var(--white);font-weight:600}
.card.is-active .more{color:var(--red)}

/* lower */
.section-title{font-size:18px;font-weight:600;color:var(--ink)}
.sources{left:73px;top:835px;width:246px;box-shadow:0 1px 4px rgba(0,0,0,.15)}
.sources li{list-style:none;height:40px;display:flex;align-items:center;justify-content:space-between;padding:0 12px 0 15px;font-size:15px;color:#444;
  background:linear-gradient(#fff,#eef4f5);border-bottom:1px solid #e1e6e7}
.sources li.active{background:var(--red);color:var(--white)}
.sources .arrow{width:22px;height:22px;border-radius:50%;border:1px solid #ccc;background:#fff;display:flex;align-items:center;justify-content:center}
.sources li.active .arrow{background:#333;border-color:#333}
.welcome-photo{left:381px;top:837px;width:166px;height:106px;background:linear-gradient(135deg,#dce6ee,#7b93ad 55,#2d3f5e)}
.welcome-photo{background:linear-gradient(135deg,#e3ebf1 0%,#9fb1c4 50%,#2e405c 100%)}
.welcome-text{left:566px;top:835px;width:364px;font-size:11.5px;line-height:18px;color:var(--ink)}
.welcome-text p+p{margin-top:2px}
.news{top:1005px;display:flex;gap:10px;font-size:11.5px;line-height:18px;color:var(--ink)}
.news-photo{width:77px;height:66px;border:1px solid #ddd;padding:2px;background:#fff}
.news-photo div{width:100%;height:100%}
.news b{font-weight:700;color:#111}

/* footer */
.footer{left:0;top:1114px;width:996px;height:86px;background:var(--footer);color:var(--white);font-size:11.5px}
.footer-links{left:73px;top:21px}
.footer-copy{left:74px;top:55px}
.social{left:735px;top:26px;display:flex;gap:9px}
.social span{width:28px;height:28px;border-radius:5px}
</style>
</head>
<body>

<header>
  <div class="abs brand">
    <div class="brand-mark"></div>
    <div>
      <div class="brand-name">Velmoran Associates</div>
      <div class="brand-tag">Trade, Investment, Market Research</div>
    </div>
  </div>
  <div class="abs search">Search..
    <svg width="12" height="12" viewBox="0 0 12 12"><circle cx="5" cy="5" r="3.8" fill="none" stroke="#888" stroke-width="1.6"/><line x1="8" y1="8" x2="11" y2="11" stroke="#888" stroke-width="1.8"/></svg>
  </div>
  <nav class="abs nav">
    <a class="active" href="#">HOME</a><a href="#">ABOUT US</a><a href="#">SERVICES</a><a href="#">TRADE</a><a href="#">CONTACT</a>
  </nav>
</header>

<section class="abs hero" role="img" aria-label="Photo of a smiling young woman working at a laptop in a bright office"></section>
<div class="abs hero-copy">
  <div class="hero-title">PROVIDING</div>
  <div class="hero-sub">LEADING BUSINESS SERVICES</div>
  <p class="hero-text">Jerta baditaut onsequser untur magni dol ores eoquie voluptate msequi nesciunt.</p>
</div>
<div class="abs dots"><span></span><span></span><span></span><span></span></div>

<section>
  <div class="abs card is-active" style="left:73px">
    <h3>Agents /<br>Representative</h3>
    <svg width="44" height="44" viewBox="0 0 44 44"><circle cx="22" cy="22" r="21" fill="#fff"/><g stroke="#c60000" stroke-width="3"><line x1="22" y1="22" x2="22" y2="1"/><line x1="22" y1="22" x2="40" y2="33"/><line x1="22" y1="22" x2="4" y2="33"/></g></svg>
    <p>Lorem ipsum dolor sitamet ingelit.Morbi ut elipsum tristi umsan. Morbi ut elit utipsum tri stiquea Pellenteisque habt.</p>
    <span class="more">READ MORE</span>
  </div>
  <div class="abs card" style="left:294px">
    <h3>Effective<br>Solutions</h3>
    <svg width="48" height="46" viewBox="0 0 48 46"><g fill="#bdbdbd"><rect x="4" y="26" width="9" height="19"/><rect x="16" y="18" width="9" height="27"/><rect x="28" y="3" width="10" height="42"/><rect x="0" y="43" width="48" height="3"/></g></svg>
    <p>Lorem ipsum dolor sitamet ingelit.Morbi ut elipsum tristi umsan. Morbi ut elit utipsum tri stiquea Pellenteisque habt.</p>
    <span class="more">READ MORE</span>
  </div>
  <div class="abs card" style="left:515px">
    <h3>Investment<br>Partners</h3>
    <svg width="48" height="48" viewBox="0 0 48 48"><g fill="#bdbdbd"><circle cx="24" cy="24" r="17"/><g id="t"><rect x="20" y="0" width="8" height="10"/><rect x="20" y="38" width="8" height="10"/><rect x="0" y="20" width="10" height="8"/><rect x="38" y="20" width="10" height="8"/></g><use href="#t" transform="rotate(45 24 24)"/></g><circle cx="24" cy="24" r="7" fill="#e8e8e8"/></svg>
    <p>Lorem ipsum dolor sitamet ingelit.Morbi ut elipsum tristi umsan. Morbi ut elit utipsum tri stiquea Pellenteisque habt.</p>
    <span class="more">READ MORE</span>
  </div>
  <div class="abs card" style="left:734px">
    <h3>Joint Venture<br>Partners</h3>
    <svg width="48" height="46" viewBox="0 0 48 46"><g fill="#bdbdbd"><path d="M17 8v-4h14v4h-3v-2h-8v2z"/><rect x="1" y="9" width="46" height="35" rx="5"/></g><rect x="1" y="22" width="46" height="2" fill="#e8e8e8"/><rect x="14" y="19" width="6" height="8" fill="#e8e8e8"/><rect x="28" y="19" width="6" height="8" fill="#e8e8e8"/></svg>
    <p>Lorem ipsum dolor sitamet ingelit.Morbi ut elipsum tristi umsan. Morbi ut elit utipsum tri stiquea Pellenteisque habt.</p>
    <span class="more">READ MORE</span>
  </div>
</section>

<section>
  <h2 class="abs section-title" style="left:73px;top:797px">Our Sources</h2>
  <ul class="abs sources">
    <li class="active">On Line Databases<span class="arrow"><svg width="8" height="6" viewBox="0 0 8 6"><path d="M0 3h7M5 1l2 2-2 2" stroke="#fff" fill="none"/></svg></span></li>
    <li>CD Rom Databases<span class="arrow"><svg width="8" height="6" viewBox="0 0 8 6"><path d="M0 3h7M5 1l2 2-2 2" stroke="#555" fill="none"/></svg></span></li>
    <li>Industry Associations<span class="arrow"><svg width="8" height="6" viewBox="0 0 8 6"><path d="M0 3h7M5 1l2 2-2 2" stroke="#555" fill="none"/></svg></span></li>
    <li>Industry Experts<span class="arrow"><svg width="8" height="6" viewBox="0 0 8 6"><path d="M0 3h7M5 1l2 2-2 2" stroke="#555" fill="none"/></svg></span></li>
    <li>Government Experts<span class="arrow"><svg width="8" height="6" viewBox="0 0 8 6"><path d="M0 3h7M5 1l2 2-2 2" stroke="#555" fill="none"/></svg></span></li>
    <li>Government Agencies<span class="arrow"><svg width="8" height="6" viewBox="0 0 8 6"><path d="M0 3h7M5 1l2 2-2 2" stroke="#555" fill="none"/></svg></span></li>
  </ul>

  <h2 class="abs section-title" style="left:379px;top:797px">Welcome</h2>
  <div class="abs welcome-photo" role="img" aria-label="Photo of business people shaking hands in an office"></div>
  <div class="abs welcome-text">
    <p>Lorem ipsum dolor sit amet, consectetur adipiscing elit. In rhoncus velit consectetur ligula rutrum vestibulum vel eget libero.</p>
    <p>orem ipsum dolor sit amet, consecitetur adipiscing elit. In rhoncus velit c onsectetur ligula rutrum vestibulum vel eget libeiro. Etiam volutpat tinci dunt placerat. Phasellus consequat nunc eget orci gravida condimentum vel ut ligula</p>
  </div>

  <h2 class="abs section-title" style="left:380px;top:975px">Latest News</h2>
  <div class="abs news" style="left:378px">
    <div class="news-photo"><div role="img" aria-label="Portrait photo of a team member" style="background:linear-gradient(135deg,#3f7a3a,#b07a4e 60%,#3a2a22)"></div></div>
    <div><b>During November 2013</b><br>our Principal Petrophysicist,Maren<br>has ben working on projects. fima<br>ny keyindustries - particularly.</div>
  </div>
  <div class="abs news" style="left:665px">
    <div class="news-photo"><div role="img" aria-label="Portrait photo of a team member" style="background:linear-gradient(135deg,#e9eef2,#c9cfd6 60%,#3a3430)"></div></div>
    <div><b>During November 2013</b><br>our Principal &nbsp;Petrophysicist,Maren<br>has ben working on projects. foim<br>my keyindustries - particularly.</div>
  </div>
</section>

<footer class="abs footer">
  <div class="abs footer-links">Home | About Us | Services | Trade and Investment | Contact</div>
  <div class="abs footer-copy">Copyrights 2013. All Rights Reserved.</div>
  <div class="abs social" aria-label="Social links">
    <span style="background:#3b5a9a"></span><span style="background:#2aa3e0"></span><span style="background:#c8231f"></span><span style="background:#1a6fae"></span>
  </div>
</footer>

</body>
</html>
```